全国の1人〜2人で営業されている理・美容室のオーナーさん方にコロナでも全く影響を受けてない当サロンのノウハウを読んで頂きたいと思っています。
これからのサロンのあり方、考え方、今すぐに取り入れるべき技術や商品、売り上げの上げ方などをお伝えします。本気で環境を変えたい方、美容師の仕事、接客、人をキレイにすることが大好きな方、意識の高いお客様に囲まれずっと通って頂けるような、そんな美容室を一緒に作って行きたいです。

この度はご提案、修正と本当にありがとうございました。最後の最後までかなり悩みました。
初めての電子書籍で良い表紙デザインと出会うことが出来ました。

今回、ご提案頂いた皆さん、本当にありがとうございました。初心者の自分に親身になって頂き、皆さんの丁寧なデザインに感動しました。また2冊目も考えています。ご縁があればまたよろしくお願いします。

```html
<!DOCTYPE html>
<html lang="ja">
<head>
<meta charset="utf-8">
<title>サロンが生き残る方法 — 表紙</title>
<link rel="stylesheet" href="https://fonts.googleapis.com/css2?family=Noto+Sans+JP:wght@500;700;900&display=swap">
<style>
  :root {
    --ink: #1a1a1a;
    --accent: #e3175e;
    --paper: #ffffff;
    --photo-warm: #b88c63;
    --photo-mid: #7d6450;
    --photo-deep: #4a3d33;
    --figure-tone: #d9e3ee;
    --bubble-line: #8c8c8c;
  }
  html, body {
    margin: 0;
    padding: 0;
    width: 750px;
    height: 1200px;
    overflow: hidden;
    background: var(--paper);
  }
  .cover {
    position: relative;
    width: 750px;
    height: 1200px;
    overflow: hidden;
    background: var(--paper);
    font-family: "Noto Sans JP", sans-serif;
    color: var(--ink);
  }
  .cover h1 { margin: 0; font-size: inherit; }
  .cover-photo {
    position: absolute;
    left: 0;
    top: 600px;
    width: 750px;
    height: 600px;
    background:
      radial-gradient(ellipse 260px 140px at 230px 360px, rgba(154,158,163,0.75), rgba(154,158,163,0) 70%),
      radial-gradient(ellipse 200px 120px at 120px 470px, rgba(70,110,70,0.45), rgba(70,110,70,0) 70%),
      linear-gradient(to bottom,
        rgba(255,255,255,1) 0%,
        rgba(255,255,255,0) 22%,
        var(--photo-warm) 40%,
        var(--photo-mid) 70%,
        var(--photo-deep) 100%);
    z-index: 0;
  }
  .vertical {
    position: absolute;
    margin: 0;
    writing-mode: vertical-rl;
    font-weight: 900;
    line-height: 1;
    white-space: nowrap;
    z-index: 2;
  }
  .subtitle {
    left: 655px;
    top: 18px;
    font-size: 70px;
    letter-spacing: -2px;
  }
  .title-lead {
    left: 515px;
    top: 140px;
    font-size: 50px;
    font-weight: 700;
  }
  .title-main {
    left: 485px;
    top: 355px;
    font-size: 104px;
  }
  .title-end {
    left: 302px;
    top: 225px;
    font-size: 104px;
  }
  .accent { color: var(--accent); }
  .particle { font-size: 86px; color: var(--ink); }
  .author {
    left: 50px;
    top: 275px;
    font-size: 40px;
    font-weight: 700;
  }
  .author-mark { margin-top: 18px; display: inline-block; font-size: 30px; }
  .speech {
    position: absolute;
    left: 405px;
    top: 762px;
    width: 225px;
    height: 150px;
    z-index: 3;
  }
  .speech svg { position: absolute; inset: 0; }
  .speech-text {
    position: absolute;
    left: 0;
    top: 10px;
    width: 225px;
    margin: 0;
    text-align: center;
    font-size: 22px;
    font-weight: 700;
    line-height: 1.3;
  }
  .figure {
    position: absolute;
    left: 512px;
    top: 912px;
    width: 135px;
    height: 260px;
    border-radius: 66px 66px 18px 18px;
    background: linear-gradient(to bottom, var(--figure-tone), #b9c8da);
    z-index: 3;
  }
</style>
</head>
<body>
  <main class="cover">
    <div class="cover-photo" role="img" aria-label="美容師のハサミやコームなど仕事道具が並ぶ写真"></div>

    <h2 class="vertical subtitle">コロナや景気に左右されない、</h2>

    <h1>
      <span class="vertical title-lead">これから</span>
      <span class="vertical title-main"><span class="accent">サロン</span><span class="particle">が</span></span>
      <span class="vertical title-end">生き残る<span class="accent">方法</span></span>
    </h1>

    <p class="vertical author">やまもと はるか<span class="author-mark">著</span></p>

    <div class="speech">
      <svg viewBox="0 0 225 150" width="225" height="150" aria-hidden="true">
        <path d="M112 3 C172 3 222 24 222 62 C222 96 188 118 150 122 L172 148 L132 124 C125 124 118 124 112 124 C52 124 3 100 3 62 C3 24 52 3 112 3 Z"
              fill="#ffffff" stroke="var(--bubble-line)" stroke-width="2"/>
      </svg>
      <p class="speech-text">小さな<br>サロンですが、<br>予約がずっと<br>続きます！</p>
    </div>

    <div class="figure" role="img" aria-label="帽子をかぶった男性スタッフのイラスト"></div>
  </main>
</body>
</html>
```